Pebble-Vane Brochure

Hello,

I want a "printed" version of the www.Pebble-Vane.net web site, so I can send it to prospect customers by physical mail.

Full Color, Letter Size paper and maximum of 8 pages.

If you need any additional information please let me know.

```html
<!DOCTYPE html>
<html lang="en">
<head>
<meta charset="utf-8">
<title>Pebble-Vane Brochure — Covers</title>
<link rel="stylesheet" href="https://fonts.googleapis.com/css2?family=Montserrat:wght@400;500;700;800&display=swap">
<style>
  :root {
    --backdrop: #ece4df;
    --paper: #ffffff;
    --navy: #2b2a6b;
    --deep-navy: #1f1d55;
    --brand-blue: #1d4f8f;
    --cyan: #1fb2ee;
    --sky: #9fcdea;
    --ink: #1b1b1f;
    --photo-light: #c9ccd2;
    --photo-mid: #8d9098;
    --photo-skin: #d9a68a;
    --photo-dark: #2a2c31;
    --blue-bright: #1e9be0;
    --blue-mid: #1566b8;
  }
  * { margin: 0; padding: 0; box-sizing: border-box; }
  html, body {
    width: 1060px;
    height: 1200px;
    overflow: hidden;
    background: var(--backdrop);
    font-family: "Montserrat", sans-serif;
  }
  .spread {
    position: absolute;
    left: 50px;
    top: 290px;
    width: 960px;
    height: 621px;
    display: flex;
    box-shadow: 0 12px 30px rgba(60, 40, 30, 0.18);
  }
  .page { width: 480px; height: 621px; display: block; }
  .brand-name { font-family: "Montserrat", sans-serif; font-weight: 700; }
  .headline { font-family: "Montserrat", sans-serif; font-weight: 800; fill: var(--ink); }
  .tagline { font-family: "Montserrat", sans-serif; font-weight: 400; fill: var(--paper); }
  .subline { font-family: "Montserrat", sans-serif; font-weight: 400; fill: var(--ink); }
  .contact { font-family: "Montserrat", sans-serif; font-weight: 400; fill: var(--paper); font-size: 9px; }
</style>
</head>
<body>
  <main class="spread">
    <!-- Back cover -->
    <svg class="page back-cover" viewBox="0 0 480 621" xmlns="http://www.w3.org/2000/svg">
      <defs>
        <linearGradient id="backBlue" x1="0" y1="0" x2="0.4" y2="1">
          <stop offset="0" stop-color="var(--blue-mid)"/>
          <stop offset="0.35" stop-color="var(--blue-bright)"/>
          <stop offset="0.7" stop-color="var(--blue-mid)"/>
          <stop offset="1" stop-color="var(--deep-navy)"/>
        </linearGradient>
        <radialGradient id="backPhoto" cx="0.7" cy="0.3" r="0.8">
          <stop offset="0" stop-color="#6a6d74"/>
          <stop offset="0.5" stop-color="#3a3c42"/>
          <stop offset="1" stop-color="var(--photo-dark)"/>
        </radialGradient>
        <clipPath id="backClip"><rect width="480" height="621"/></clipPath>
      </defs>
      <g clip-path="url(#backClip)">
        <rect class="back-field" width="480" height="621" fill="url(#backBlue)"/>
        <circle class="arc-ring-light" cx="575" cy="150" r="352" fill="var(--sky)"/>
        <circle class="arc-ring" cx="575" cy="150" r="344" fill="var(--paper)"/>
        <circle class="back-photo" cx="575" cy="150" r="322" fill="url(#backPhoto)"
                role="img" aria-label="Blurred close-up photo of glowing network icons on a dark background"/>
      </g>
      <g class="back-contact">
        <text class="contact" x="330" y="520">1420 Harbor Lane, Suite</text>
        <text class="contact" x="330" y="532">210 Unit B</text>
        <text class="contact" x="330" y="548">Lakeview, FL, 33000</text>
        <text class="contact" x="330" y="564">sales@pebble-vane.net</text>
        <text class="contact" x="330" y="580">www.Pebble-Vane.net</text>
      </g>
      <g class="back-brand">
        <circle cx="56" cy="568" r="12" fill="var(--sky)"/>
        <text class="brand-name" x="76" y="575" font-size="20" fill="var(--sky)">Pebble-Vane</text>
      </g>
    </svg>

    <!-- Front cover -->
    <svg class="page front-cover" viewBox="0 0 480 621" xmlns="http://www.w3.org/2000/svg">
      <defs>
        <radialGradient id="frontPhoto" cx="0.45" cy="0.6" r="0.75">
          <stop offset="0" stop-color="var(--photo-skin)"/>
          <stop offset="0.35" stop-color="#b99b8c"/>
          <stop offset="0.7" stop-color="var(--photo-mid)"/>
          <stop offset="1" stop-color="#5a5d65"/>
        </radialGradient>
      </defs>
      <rect class="paper" width="480" height="621" fill="var(--paper)"/>
      <g class="front-brand">
        <circle cx="170" cy="50" r="12" fill="var(--brand-blue)"/>
        <text class="brand-name" x="190" y="58" font-size="22" fill="var(--brand-blue)">Pebble-Vane</text>
      </g>
      <rect class="front-photo" x="0" y="92" width="480" height="300" fill="url(#frontPhoto)"
            role="img" aria-label="Photo of a hand touching a glowing cloud icon surrounded by a network of app icons"/>
      <g class="cover-title" text-anchor="end">
        <text class="headline" x="455" y="430" font-size="17">Create your own Private Cloud,</text>
        <rect class="tagline-box" x="215" y="441" width="240" height="36" fill="var(--cyan)"/>
        <text class="tagline" x="448" y="469" font-size="27">Brick by Brick</text>
        <text class="subline" x="455" y="500" font-size="16">Virtual Data Center on dedicated</text>
        <text class="subline" x="455" y="519" font-size="16">Hardware</text>
      </g>
      <path class="swoosh-line" d="M0 548 Q220 585 420 621 L400 621 Q210 590 0 556 Z" fill="var(--sky)"/>
      <path class="swoosh" d="M0 562 Q200 595 380 621 L0 621 Z" fill="var(--navy)"/>
    </svg>
  </main>
</body>
</html>
```